Gourmet's Wander Through France Brochure

We need a brochure design for Table Verdane, a boutique culinary travel company. We specialize in all-inclusive cooking vacations to the Southwest of France for curious foodies.
More projects to follow if successful.
See website at http://www.tableverdane.example

Target Market(s)

Predominantly middle-aged women in the US

Industry/Entity Type

Boutique

Requirements
Must have
• Brochure should be standard 8.5"x11" tri-fold, double-sided.

Must have:
- tagline: A Gourmet's Wander Through France
- visual invitation to travel - include a selection from the pictures provided.

- a clean, sophisticated feel.

- two major design elements: green color (see attached logo) and triangular shape (which represents the Pyrenees mountains).

Main focus should be on three main axes of the trip (see attached text):
- Enrich (cooking classes)
- Interact (with artisans)
- Explore (visits).

Side information should include:
- Hosts
- Accommodations
- What is included
- Location (map)
- Contact Info (phone/email/website)
Nice to have
• If possible, brochure in an MS Office format for future edits.

```html
<!DOCTYPE html>
<html lang="en">
<head>
<meta charset="utf-8">
<title>Table Verdane – Brochure</title>
<link rel="stylesheet" href="https://fonts.googleapis.com/css2?family=Source+Sans+3:wght@400;600;700&display=swap">
<style>
  :root {
    --page-bg: #ffffff;
    --sheet-white: #ffffff;
    --green-top: #d0cc3a;
    --green-mid: #b4b43c;
    --green-bottom: #96a042;
    --brand-green: #a9bf2f;
    --ink: #222222;
    --ink-soft: #555555;
    --white: #ffffff;
    --map-sea: #8fd6f0;
    --map-land: #e6eaa8;
  }
  * { box-sizing: border-box; margin: 0; padding: 0; }
  html, body {
    width: 1200px; height: 950px; overflow: hidden;
    background: var(--page-bg);
    font-family: "Source Sans 3", sans-serif;
  }
  .sheet {
    position: absolute; left: 50px; top: 50px;
    width: 1100px; height: 850px;
    background: var(--sheet-white);
    box-shadow: 3px 4px 8px rgba(0,0,0,0.35);
    overflow: hidden;
  }
  .sheet__band {
    position: absolute; left: 0; top: 193px; width: 1100px; height: 657px;
    background: linear-gradient(180deg, var(--green-top) 0%, var(--green-mid) 50%, var(--green-bottom) 100%);
  }
  .intro {
    position: absolute; left: 36px; top: 45px; width: 320px; white-space: nowrap;
    font-size: 15px; font-weight: 700; line-height: 19.5px; color: var(--ink);
  }
  .brand { position: absolute; top: 120px; width: 260px; text-align: center; }
  .brand--middle { left: 420px; }
  .brand--right { left: 786px; }
  .brand__name {
    font-size: 24px; font-weight: 600; color: var(--brand-green); line-height: 28px;
    display: flex; align-items: center; justify-content: center; gap: 8px;
  }
  .brand__dot { width: 10px; height: 10px; background: var(--brand-green); border-radius: 50%; }
  .brand__line { font-size: 14px; color: var(--ink-soft); margin-top: 3px; }

  .block { position: absolute; left: 36px; color: var(--white); white-space: nowrap; }
  .section-title { font-size: 17px; font-weight: 700; line-height: 20px; }
  .body-text { font-size: 15px; line-height: 19px; }
  .title--included { top: 206px; }
  .included { top: 230px; list-style: none; }
  .included li { position: relative; padding-left: 15px; margin-bottom: 3.5px; }
  .included li::before { content: "•"; position: absolute; left: 0; }
  .title--hosts { top: 440px; }
  .host--first { top: 465px; }
  .host--second { top: 562px; }
  .host__name { font-weight: 700; }
  .host__photo {
    position: absolute; left: 239px; width: 92px; height: 88px;
    border: 2px solid var(--white); border-radius: 4px;
  }
  .host__photo--chef { top: 468px; background: linear-gradient(135deg, #b7ada0, #5a5248); }
  .host__photo--guide { top: 566px; background: linear-gradient(135deg, #d7ccb8, #6d6358); }
  .title--accommodation { top: 677px; }
  .accommodation { top: 702px; }

  .map {
    position: absolute; left: 403px; top: 208px; width: 295px; height: 197px;
    border: 3px solid var(--white); border-radius: 10px;
    background: linear-gradient(115deg, var(--map-land) 0%, #a9c25a 40%, #e8e8e8 55%, var(--map-sea) 70%);
  }
  .contact { position: absolute; left: 400px; top: 430px; width: 300px; text-align: center; color: var(--white); font-weight: 700; }
  .contact__head { font-size: 23px; line-height: 29px; }
  .contact__sub { font-size: 17px; margin-top: 10px; }
  .contact__details { font-size: 17px; line-height: 22px; margin-top: 14px; }

  .gallery { position: absolute; left: 769px; top: 209px; display: grid; grid-template-columns: repeat(3, 93px); gap: 8px; }
  .gallery--lower { top: 575px; }
  .photo { height: 77px; border: 2px solid var(--white); border-radius: 5px; }
  .photo--warm { background: linear-gradient(135deg, #b38a63, #4c382a); }
  .photo--cool { background: linear-gradient(135deg, #a5b79a, #4f5f45); }
  .photo--red { background: linear-gradient(135deg, #c4463a, #5a2a22); }
  .photo--sky { background: linear-gradient(180deg, #9fb9d4, #6e8f5e); }
  .feature {
    position: absolute; left: 769px; top: 464px; width: 295px; height: 101px;
    background: var(--white); border-radius: 6px;
    display: flex; align-items: center; justify-content: center; text-align: center;
    font-size: 29px; font-weight: 600; line-height: 31px; color: var(--brand-green);
  }
</style>
</head>
<body>
<div class="sheet">
  <div class="sheet__band"></div>

  <p class="intro">You understand that the trip of a lifetime<br>isn’t a passive experience. With your<br>personal guide, get ready to immerse<br>in the exquisite culture and lifestyle of<br>the French Paradox in the southwestern<br>region of France.</p>

  <div class="brand brand--middle">
    <div class="brand__name"><span class="brand__dot"></span>Table Verdane</div>
    <div class="brand__line">Cooking Holidays in Southwest France</div>
  </div>
  <div class="brand brand--right">
    <div class="brand__name"><span class="brand__dot"></span>Table Verdane</div>
    <div class="brand__line">Cooking Holidays in Southwest France</div>
  </div>

  <h2 class="block section-title title--included">What is Included</h2>
  <ul class="block body-text included">
    <li>Eight nights’ accommodation</li>
    <li>All meals and wine pairings from<br>Bonjour! to Bon Voyage!</li>
    <li>Your full-time English-speaking guide</li>
    <li>Private local transportation and<br>airport transfers</li>
    <li>Four half-day hands-on cooking classes</li>
    <li>All materials and entrance fees to<br>scheduled activities and events</li>
  </ul>

  <h2 class="block section-title title--hosts">Your hosts</h2>
  <p class="block body-text host--first"><span class="host__name">Chef Laurent Dubreuil</span><br>30 years’ culinary experience.<br>Owner and Chef de Cuisine,<br>Auberge du Vallon,<br>since 2004.</p>
  <div class="host__photo host__photo--chef" role="img" aria-label="Portrait photo of the chef in his kitchen"></div>
  <p class="block body-text host--second"><span class="host__name">Céline Marchand</span><br>Well-traveled French native<br>with English fluency.<br>Extensive knowledge of<br>southwest France.</p>
  <div class="host__photo host__photo--guide" role="img" aria-label="Portrait photo of the tour guide"></div>

  <h2 class="block section-title title--accommodation">Accommodation</h2>
  <p class="block body-text accommodation">Enjoy modern accommodation throughout<br>the tour, starting with a stay at a boutique<br>hotel in Toulouse for a taste of a French<br>metropolis. Continue your getaway in an<br>exquisitely renovated medieval stone chateau<br>in the foothills of the Pyrenees mountains.</p>

  <div class="map" role="img" aria-label="Map of southwestern France showing Toulouse, Carcassonne, the Pyrenees and the Mediterranean Sea, with an inset of France"></div>

  <div class="contact">
    <p class="contact__head">Have questions?<br>Ready to book?</p>
    <p class="contact__sub">We’d love to hear from you</p>
    <p class="contact__details">(312) 555-0147<br>info@tableverdane.example<br>www.tableverdane.example</p>
  </div>

  <div class="gallery">
    <div class="photo photo--warm" role="img" aria-label="Guests at a cooking class"></div>
    <div class="photo photo--red" role="img" aria-label="Red wine being poured"></div>
    <div class="photo photo--warm" role="img" aria-label="Cook preparing food"></div>
    <div class="photo photo--warm" role="img" aria-label="Tray of custard desserts"></div>
    <div class="photo photo--cool" role="img" aria-label="Market stall of vegetables"></div>
    <div class="photo photo--warm" role="img" aria-label="Winemaker with bottles"></div>
    <div class="photo photo--sky" role="img" aria-label="Vineyard landscape"></div>
    <div class="photo photo--red" role="img" aria-label="Basket of fresh vegetables"></div>
    <div class="photo photo--warm" role="img" aria-label="Old stone kitchen interior"></div>
  </div>

  <div class="feature">A Gourmet’s Wander<br>Through France</div>

  <div class="gallery gallery--lower">
    <div class="photo photo--sky" role="img" aria-label="Brick basilica in Toulouse"></div>
    <div class="photo photo--cool" role="img" aria-label="Asparagus at a market"></div>
    <div class="photo photo--warm" role="img" aria-label="Chef at work in apron"></div>
    <div class="photo photo--warm" role="img" aria-label="Chocolate desserts being served"></div>
    <div class="photo photo--cool" role="img" aria-label="Guests dining outdoors"></div>
    <div class="photo photo--warm" role="img" aria-label="Hands preparing a dish"></div>
    <div class="photo photo--sky" role="img" aria-label="Pyrenees mountain view"></div>
    <div class="photo photo--warm" role="img" aria-label="Wine bottles on a table"></div>
    <div class="photo photo--red" role="img" aria-label="Market stall of red fruit"></div>
  </div>
</div>
</body>
</html>
```